Harborline Kidney Services Brochure - Marketing brochure for a dialysis company in the USA

I want a brochure to be created for my business. I have a brochure that can be used as a comparison. My old Company name is Harborline Kidney Services. The new Company Name is Harborline Kidney Services. I have a sample of the Old Brochure. and I uploaded the Logo of HKS. It will be used by my sales agents to introduce my company to potential client hospitals.

Target Market(s)

CEOs of Acute Hospitals and Medical Centers

Industry/Entity Type

Health Care

Requirements
Must have
• Use the sample as a guide. This project is for a 4 page brochure. (2 letter size pages folded in half crosswise) Use the text from the old brochure to the new brochure, replacing the old info with the new company info as needed.
Nice to have
• Here is my company info:
• Harborline Kidney Services
• 4180 W 61st Ave
• Suite D
• It will be nice if the designer can give me the project files that would allow me to edit the text of the brochure.
• McAllen, TX 78392
• (956) 417-2863
• admin@HarborlineKidneyLLC.example
• www.harborlinekidney.example

```html
<!DOCTYPE html>
<html lang="en">
<head>
<meta charset="utf-8">
<title>Harborline Kidney Services Brochure</title>
<link rel="stylesheet" href="https://fonts.googleapis.com/css2?family=Fira+Sans+Condensed:wght@600;700&family=Source+Sans+3:wght@400;600;700&display=swap">
<style>
:root{
  --stage:#3b3b3d;
  --navy:#1c2f86;
  --blue:#2a63c4;
  --sky:#8fc3ef;
  --pale:#e6f2fc;
  --red:#d3222a;
  --ink:#333;
  --grey-box:#ececec;
  --silver:#c9ccd1;
}
*{margin:0;padding:0;box-sizing:border-box}
html,body{width:1200px;height:1200px;overflow:hidden;background:var(--stage)}
body{position:relative;font-family:"Source Sans 3",sans-serif;color:var(--ink)}
.spread{position:absolute;overflow:hidden}
.abs{position:absolute}
.ph{position:absolute}

/* cover spread */
.cover{left:254px;top:36px;width:692px;height:534px;
  background:radial-gradient(ellipse 260px 300px at 520px 230px,#fff 0%,var(--pale) 40%,var(--sky) 80%,var(--blue) 110%),var(--blue)}
.cover .fold{position:absolute;left:345px;top:0;width:2px;height:100%;background:rgba(255,255,255,.5)}
.silver-band{left:0;top:62px;width:692px;height:26px;
  background:linear-gradient(#f4f5f7,#9ea3aa 45%,#fff 55%,#b5b9bf)}
.brand-plate{top:54px;width:210px;height:42px;background:var(--navy);border-radius:4px;
  display:flex;align-items:center;justify-content:center;color:#fff;
  font:700 15px "Source Sans 3",sans-serif;letter-spacing:.3px}
.hero-photo{left:0;top:98px;width:346px;height:240px;
  background:linear-gradient(160deg,#cfe3f4,#8db8de 60%,#b7d4ee)}
.contact{left:0;top:370px;width:346px;font-size:10px;line-height:12.6px;color:#2a2a2a}
.contact .addr{position:absolute;right:190px;text-align:right;white-space:nowrap}
.contact .addr b{color:var(--red);font-weight:600}
.contact .rule{position:absolute;left:162px;top:1px;width:1px;height:37px;background:#222}
.contact .lines{position:absolute;left:170px;white-space:nowrap}
.headline{left:346px;top:144px;width:346px;text-align:center;
  font:700 24px/31px "Fira Sans Condensed",sans-serif;color:var(--navy)}
.machine-img{left:402px;top:244px;width:62px;height:164px;border-radius:6px;
  background:linear-gradient(#e8ecf0,#c6ccd4)}
.kidney-img{left:478px;top:304px;width:148px;height:100px;border-radius:40px;
  background:linear-gradient(90deg,#d9394a,#5a6fc8 50%,#d9394a)}
.call{top:428px;font:700 14px/17px "Source Sans 3",sans-serif;color:#111}
.call strong{display:block;font-size:19px;line-height:22px;color:var(--red)}
.call.left{right:376px;text-align:right}
.call.right{left:378px}
.cover-wave{left:0;top:470px}
.cover-url{top:516px;font:700 9.5px "Fira Sans Condensed",sans-serif;color:#fff}

/* inner spread */
.inner{left:251px;top:625px;width:698px;height:539px;background:#fff}
.inner-head{left:0;top:0}
.name-mark{top:44px;font:700 13px/14px "Source Sans 3",sans-serif;color:var(--navy)}
h2{font:700 8.2px/10.6px "Fira Sans Condensed",sans-serif;color:var(--navy)}
.body{font-size:7.3px;line-height:9.6px;text-align:justify;color:#444}
.body p+p{margin-top:7px}
.framed{border:1.5px solid var(--navy)}
.q-box{left:25px;top:411px;width:170px;height:74px;background:var(--grey-box);padding:6px 6px}
.q-box h2{margin-bottom:7px}
.points{left:379px;top:175px;width:280px;list-style:none;counter-reset:n}
.points li{position:relative;padding-left:14px;margin-bottom:8px;counter-increment:n}
.points li::before{content:counter(n);position:absolute;left:0;top:0;width:10px;height:10px;border-radius:50%;
  background:var(--red);color:#fff;font:700 6.5px/10px "Source Sans 3",sans-serif;text-align:center}
.foot-rule{left:0;top:503px;width:698px;height:2px;background:var(--red)}
.page-no{top:506px;width:22px;height:21px;background:var(--red);color:#fff;font-size:7px;line-height:21px;text-align:center}
.foot-url{top:512px;font-size:6.5px;letter-spacing:.8px;color:#333}
</style>
</head>
<body>

<section class="spread cover">
  <div class="fold"></div>
  <div class="abs silver-band"></div>
  <div class="abs brand-plate" style="left:65px">Harborline Kidney Services</div>
  <div class="abs brand-plate" style="left:415px">Harborline Kidney Services</div>

  <div class="ph hero-photo" role="img" aria-label="Hospital intensive care room with bed and dialysis equipment"></div>

  <div class="abs contact">
    <div class="addr"><b>Harborline Kidney Services</b><br>4180 W 61st Ave &nbsp;Suite D<br>McAllen, TX 78392</div>
    <div class="rule"></div>
    <div class="lines">(956) 417-2863<br>admin@HarborlineKidneyLLC.example<br>www.harborlinekidney.example</div>
  </div>

  <h1 class="abs headline">Tired of Paying Outrageous<br>Prices for inpatient dialysis?</h1>
  <div class="ph machine-img" role="img" aria-label="Hemodialysis machine"></div>
  <div class="ph kidney-img" role="img" aria-label="Illustration of a pair of kidneys"></div>

  <svg class="abs cover-wave" width="692" height="64" viewBox="0 0 692 64" aria-hidden="true">
    <path d="M0 2 Q173 8 346 26 Q519 8 692 2 L692 64 L0 64Z" fill="#ffffff"/>
    <path d="M0 6 Q173 12 346 30 Q519 12 692 6 L692 64 L0 64Z" fill="var(--red)"/>
    <path d="M0 13 Q173 19 346 37 Q519 19 692 13 L692 64 L0 64Z" fill="var(--blue)"/>
    <path d="M0 30 Q346 40 692 30 L692 64 L0 64Z" fill="var(--navy)" opacity=".6"/>
  </svg>
  <div class="abs call left">Call us now!!!<strong>(956) 417-2863</strong></div>
  <div class="abs call right">Call us now!!!<strong>(956) 417-2863</strong></div>
  <div class="abs cover-url" style="left:12px">www.harborlinekidney.example</div>
  <div class="abs cover-url" style="right:14px">www.harborlinekidney.example</div>
</section>

<section class="spread inner">
  <svg class="abs inner-head" width="698" height="72" viewBox="0 0 698 72" aria-hidden="true">
    <defs>
      <linearGradient id="headFill" x1="0" y1="0" x2="0" y2="1">
        <stop offset="0" stop-color="#26379a"/><stop offset="1" stop-color="#6f9ad8"/>
      </linearGradient>
    </defs>
    <rect width="698" height="72" fill="url(#headFill)"/>
    <rect x="250" width="200" height="60" fill="#a9c4ea" opacity=".55" role="img" aria-label="Dialysis tubing photograph"/>
    <path d="M0 38 Q200 32 349 62 Q498 32 698 38" fill="none" stroke="var(--red)" stroke-width="5"/>
    <path d="M0 42 Q200 36 349 66 Q498 36 698 42 L698 72 L0 72Z" fill="#fff"/>
  </svg>
  <div class="abs name-mark" style="left:33px">Harborline Kidney Services</div>
  <div class="abs name-mark" style="right:26px">Harborline Kidney Services</div>

  <div class="abs" style="left:25px;top:88px;width:144px">
    <h2>Who is Harborline Kidney Services LLC (HKS) and what services does it provide?</h2>
    <div class="body" style="margin-top:10px">
      <p>HKS is the lowest cost, highest quality inpatient dialysis and related services provider in South Texas. HKS has achieved its excellent reputation by offering performance instead of promises.</p>
      <p>Any company can tell you that they provide excellent service. Let us show you truly excellent service instead!</p>
    </div>
  </div>
  <div class="ph framed" style="left:181px;top:88px;width:144px;height:91px;background:linear-gradient(135deg,#cdd8e4,#8fa4bc)" role="img" aria-label="Dialysis machine tubing at a patient bedside"></div>
  <div class="ph" style="left:57px;top:214px;width:76px;height:186px;border-radius:6px;background:linear-gradient(#eef1f4,#c3c9d1)" role="img" aria-label="Hemodialysis machine"></div>

  <div class="abs" style="left:180px;top:199px;width:145px">
    <h2>Our facility currently contracts with another dialysis services provider. Why should we switch to HKS?</h2>
    <div class="body" style="margin-top:6px">
      <p>HKS specializes in inpatient dialysis only. Your current provider specializes in outpatient, clinic-based dialysis, and sends poorly qualified staff from their clinic to your facility to dialyze your often medically complex and hemodynamically unstable hospitalized patients. Contracting with a company that specializes in outpatient, clinic based dialysis to dialyze your inpatient dialysis patient population is similar to hiring a general practitioner to do neurosurgery.</p>
      <p>Inpatient acute dialysis is a specialty, with much sicker and medically unstable clients than an outpatient dialysis clinic, and is best handled by a company that specializes ONLY in inpatient acute dialysis and related inpatient services.</p>
    </div>
  </div>

  <div class="abs q-box">
    <h2>What types of facilities typically contract with HKS?</h2>
    <div class="body" style="text-align:left">All types of inpatient facilities can contract with HKS, including large university medical centers, small community hospitals, long term acute care hospitals, and rehabilitation hospitals.</div>
  </div>
  <div class="ph framed" style="left:203px;top:411px;width:123px;height:74px;background:linear-gradient(135deg,#e7c9b8,#8c8fc9)" role="img" aria-label="Nurse attending to dialysis equipment"></div>

  <h2 class="abs" style="left:373px;top:93px">How is Harborline Kidney Services LLC different from its competitors?</h2>
  <div class="ph" style="left:373px;top:104px;width:300px;height:65px;background:linear-gradient(90deg,#9ec9cc,#e4d7da 45%,#c9e4ea)" role="img" aria-label="Close-up of blood filter on dialysis machine"></div>

  <ol class="abs points body">
    <li>We are based in South Texas. Our two main competitors are based in California and Massachusetts. When you have a question or concern, you can contact the president and founder of HKS by mobile phone, 24 hours a day, 7 days a week. You cannot do this with any of our competitors.</li>
    <li>Acute inpatient dialysis and related services is our <b>ONLY</b> business. We perform these treatments using cutting edge dialysis equipment. 95% of the business of our competitors comes from their outpatient hemodialysis clinics. Our competitors view their inpatient dialysis programs as “cash cows” that supplement the meager earnings of their outpatient dialysis clinics. They use their newest dialysis machines in their outpatient clinics, and send their outdated, discontinued equipment to their inpatient dialysis programs. Quite simply, inpatient dialysis is not their priority.</li>
    <li>We strive to seamlessly integrate with your patient care staff. One of our competitors requires a hospital ICU nurse to stand at the bedside with the dialysis staff member during the entire bedside dialysis treatment in the ICU. Such a practice is not only ridiculous, it is an added expense for your facility. Such a practice would never occur with HKS.</li>
    <li>We are committed to being an ethical partner. We realize that finding nurses for hire is sometimes challenging. Therefore, we make it a point not to hire away nurses from the facilities with which we contract.</li>
    <li>We place tremendous power in the hands of our frontline managers. Unlike our competitors, when equipment and other resources are needed, our frontline managers don’t have to go through fifteen layers of middle management to get what they need. They simply call our president or vice president, and a decision is made quickly and locally.</li>
    <li>We offer more inpatient services more cost effectively than any of our competitors. Our inpatient services include hemodialysis, peritoneal dialysis, continuous venovenous hemodialysis (CVVH), therapeutic apheresis, PICC line insertion, and hemoperfusion.</li>
  </ol>

  <div class="abs foot-rule"></div>
  <div class="abs page-no" style="left:25px">02</div>
  <div class="abs page-no" style="right:25px">03</div>
  <div class="abs foot-url" style="right:364px">www.harborlinekidney.example</div>
  <div class="abs foot-url" style="left:373px">www.harborlinekidney.example</div>
</section>

</body>
</html>
```